Bref créative
Safety products company
Safety products for life
Professional
Gordon R Pike
President/Founder
482 Wexley Lane
Marlow Hollow, PA 16224-3871
866.41C.TOWN (412.8696)
pike@corvantahome.com
www.corvantahome.com
BE PREPARED
HOME
DISASTER
CHILD
SENIOR
PET
TRAVEL
STAY READY
the logo
"stacked" logo - two more will be coming with white backgrounds as soon as I receive them
4 AI LOGOS

```html
<!DOCTYPE html>
<html lang="en">
<head>
<meta charset="utf-8">
<title>Corvanta Home Stationery</title>
<link href="https://fonts.googleapis.com/css2?family=Montserrat:wght@400;600;700&display=swap" rel="stylesheet">
<style>
:root{
  --backdrop:#2b2b2b;
  --paper:#ffffff;
  --red:#c0272d;
  --red-dark:#7e1418;
  --grey:#9a9a9a;
  --grey-light:#d6d6d6;
  --ink:#444444;
  --faint:#f6e3e3;
}
*{margin:0;padding:0;box-sizing:border-box}
html,body{width:1200px;height:314px;overflow:hidden;background:var(--backdrop);font-family:"Montserrat",sans-serif}
.canvas{position:relative;width:1200px;height:314px}
.piece{position:absolute;background:var(--paper);overflow:hidden;box-shadow:0 1px 4px rgba(0,0,0,.5)}
.piece svg.art{position:absolute;left:0;width:100%}
.brand{position:absolute;display:flex;align-items:center;gap:3px;color:var(--red);font-weight:700;letter-spacing:.3px;white-space:nowrap}
.brand i{display:block;background:var(--red);border-radius:50%}
.faint-mark{position:absolute;background:var(--faint);border-radius:50%}
.small{position:absolute;color:var(--ink);font-size:3px;line-height:1.35;white-space:nowrap}
/* cards */
.card{width:96px;height:54px}
.card .brand{font-size:6px;left:8px;top:9px}
.card .brand i{width:5px;height:5px}
.card--dark{background:#3a3a3a}
/* letterhead */
.letterhead{top:12px;width:168px;height:276px}
.letterhead .brand{font-size:8px;left:14px;top:16px}
.letterhead .brand i{width:7px;height:7px}
.letterhead .faint-mark{width:56px;height:56px;left:56px;top:110px}
/* envelopes */
.envelope .brand{font-size:6.5px;left:10px;top:10px}
.envelope .brand i{width:6px;height:6px}
</style>
</head>
<body>
<main class="canvas">

  <!-- business cards -->
  <section class="piece card" style="left:12px;top:120px">
    <div class="brand"><i></i>CORVANTA HOME</div>
    <svg class="art" style="bottom:0;height:14px" viewBox="0 0 100 14" preserveAspectRatio="none">
      <path d="M0 8 Q50 0 100 6 L100 14 L0 14Z" fill="var(--grey-light)"/>
      <path d="M0 11 Q50 4 100 10 L100 14 L0 14Z" fill="var(--red)"/>
    </svg>
  </section>
  <section class="piece card" style="left:120px;top:120px">
    <div class="brand" style="top:6px"><i></i>CORVANTA HOME</div>
    <p class="small" style="left:8px;top:18px"><b>Gordon R Pike</b><br>President/Founder</p>
    <p class="small" style="left:48px;top:28px">482 Wexley Lane<br>Marlow Hollow, PA 16224-3871<br>866.41C.TOWN (412.8696)<br>pike@corvantahome.com<br>www.corvantahome.com</p>
  </section>
  <section class="piece card card--dark" style="left:12px;top:180px">
    <svg class="art" style="top:0;height:54px" viewBox="0 0 100 54" preserveAspectRatio="none">
      <path d="M0 0 H100 V14 Q50 26 0 12Z" fill="var(--red)"/>
      <circle cx="50" cy="34" r="8" fill="var(--red)"/>
    </svg>
  </section>
  <section class="piece card" style="left:120px;top:180px">
    <p class="small" style="left:10px;top:14px;color:var(--red);font-size:5px;font-weight:700">BE PREPARED</p>
    <p class="small" style="left:10px;top:24px">HOME · DISASTER · CHILD<br>SENIOR · PET · TRAVEL<br><b style="color:var(--red)">STAY READY</b></p>
    <svg class="art" style="bottom:0;height:10px" viewBox="0 0 100 10" preserveAspectRatio="none">
      <path d="M0 6 Q50 0 100 5 L100 10 L0 10Z" fill="var(--red)"/>
    </svg>
  </section>

  <!-- letterheads -->
  <section class="piece letterhead" style="left:235px">
    <svg class="art" style="top:0;height:40px" viewBox="0 0 100 40" preserveAspectRatio="none">
      <path d="M35 0 H100 V22 Q70 6 35 0Z" fill="var(--grey-light)"/>
      <path d="M55 0 H100 V14 Q80 3 55 0Z" fill="var(--red)"/>
    </svg>
    <div class="brand"><i></i>CORVANTA HOME</div>
    <div class="faint-mark"></div>
    <svg class="art" style="bottom:0;height:36px" viewBox="0 0 100 36" preserveAspectRatio="none">
      <path d="M0 14 Q50 0 100 18 L100 36 L0 36Z" fill="var(--grey-light)"/>
      <path d="M0 22 Q50 8 100 26 L100 36 L0 36Z" fill="var(--red)"/>
    </svg>
  </section>
  <section class="piece letterhead" style="left:422px">
    <div class="faint-mark" style="top:40px"></div>
    <p class="small" style="left:30px;top:250px;color:var(--grey)">482 Wexley Lane · Marlow Hollow, PA 16224-3871 · 866.41C.TOWN</p>
    <svg class="art" style="bottom:0;height:18px" viewBox="0 0 100 18" preserveAspectRatio="none">
      <path d="M0 10 Q50 0 100 10 L100 18 L0 18Z" fill="var(--red)"/>
    </svg>
  </section>

  <!-- envelopes front -->
  <section class="piece envelope" style="left:612px;top:60px;width:180px;height:112px">
    <svg class="art" style="top:0;height:112px" viewBox="0 0 180 112" preserveAspectRatio="none">
      <path d="M100 0 H180 V40 Q150 10 100 0Z" fill="var(--grey-light)"/>
      <path d="M130 0 H180 V24 Q160 6 130 0Z" fill="var(--red)"/>
      <path d="M0 96 Q90 80 180 100 V112 H0Z" fill="var(--red)"/>
    </svg>
    <div class="brand"><i></i>CORVANTA HOME</div>
    <p class="small" style="left:10px;top:22px">482 Wexley Lane<br>Marlow Hollow, PA 16224-3871</p>
  </section>
  <section class="piece envelope" style="left:612px;top:211px;width:180px;height:74px">
    <svg class="art" style="top:0;height:74px" viewBox="0 0 180 74" preserveAspectRatio="none">
      <path d="M110 0 H180 V30 Q150 8 110 0Z" fill="var(--grey-light)"/>
      <path d="M0 62 Q90 50 180 64 V74 H0Z" fill="var(--red)"/>
    </svg>
    <div class="brand"><i></i>CORVANTA HOME</div>
    <p class="small" style="left:10px;top:22px">482 Wexley Lane<br>Marlow Hollow, PA 16224-3871</p>
  </section>

  <!-- envelope backs -->
  <section class="piece" style="left:821px;top:12px;width:367px;height:120px;background:var(--red-dark)">
    <svg class="art" style="top:0;height:120px" viewBox="0 0 367 120" preserveAspectRatio="none">
      <rect width="367" height="120" fill="var(--red)"/>
      <path d="M0 0 H367 L183 70Z" fill="var(--red-dark)"/>
      <path d="M20 70 L183 30 L347 70 V120 H20Z" fill="var(--grey)"/>
      <path d="M0 120 L183 80 L367 120Z" fill="var(--grey-light)"/>
      <circle cx="183" cy="80" r="9" fill="var(--red)"/>
    </svg>
  </section>
  <section class="piece" style="left:821px;top:149px;width:367px;height:151px">
    <svg class="art" style="top:0;height:151px" viewBox="0 0 367 151" preserveAspectRatio="none">
      <path d="M0 0 L183 80 L367 0" fill="none" stroke="var(--grey-light)" stroke-width="1.5"/>
      <path d="M0 151 L183 90 L367 151" fill="none" stroke="var(--grey-light)" stroke-width="1.5"/>
      <circle cx="183" cy="84" r="9" fill="var(--red)"/>
    </svg>
  </section>

</main>
</body>
</html>
```